Epic Fantasy Book Cover Typography

I have some great cover art for a book cover, but need professional typography added to display the title and author name.

I have included three samples of the book title and author name I did myself in Google Picaso in a few minutes.

Target Market(s)

This will be used on a self-published epic fantasy novel, set in a medieval setting.

Requirements
Must have
• The title must be shown: Thorns Beneath Winter Ash
The author must be shown: Merrick Tolvane

PLEASE USE THE SUPPLIED ARTWORK - I'm only after the typography. However, you are welcome to adjust the colours on the art or modify as required to make the typography stand out. I am open to black and white/sepia too.

```html
<!DOCTYPE html>
<html lang="en">
<head>
<meta charset="utf-8">
<title>Thorns Beneath Winter Ash — Cover Wrap</title>
<link href="https://fonts.googleapis.com/css2?family=Cinzel:wght@400;700&family=Cinzel+Decorative:wght@700;900&family=EB+Garamond:wght@400&display=swap" rel="stylesheet">
<style>
  :root {
    --backdrop: #e4e4e4;
    --ink-dark: #1b1817;
    --spine: #151313;
    --gold-light: #f3e2a8;
    --gold-mid: #c9a35a;
    --gold-deep: #7a5a26;
    --paper-white: #f4f1ea;
    --body-text: #e8dfcf;
    --fire-bright: #f7d56a;
    --fire-orange: #c8641e;
    --smoke: #3a2a20;
  }
  * { margin: 0; padding: 0; box-sizing: border-box; }
  html, body { width: 1200px; height: 857px; overflow: hidden; background: var(--backdrop); }
  .canvas { position: relative; width: 1200px; height: 857px; }
  .wrap {
    position: absolute; left: 65px; top: 45px;
    width: 1070px; height: 767px;
    display: flex;
  }

  /* back cover */
  .back-cover {
    position: relative; width: 505px; height: 100%;
    background: var(--ink-dark); overflow: hidden;
  }
  .back-art {
    position: absolute; inset: 0 0 auto 0; height: 62%;
    background:
      radial-gradient(ellipse 70% 45% at 60% 70%, rgba(247,213,106,.55), transparent 70%),
      linear-gradient(180deg, #2a201b 0%, #5a3a22 40%, #8a6230 70%, var(--ink-dark) 100%);
  }
  .back-title { position: absolute; top: 44px; left: 0; right: 0; text-align: center; }
  .back-body {
    position: absolute; top: 170px; left: 42px; right: 36px;
    font-family: "EB Garamond", serif; font-size: 11.5px; line-height: 1.6;
    color: var(--body-text);
  }
  .back-body p + p { margin-top: 14px; }
  .back-author {
    position: absolute; top: 500px; left: 150px; right: 30px;
    font-family: "Cinzel", serif; font-size: 21px; color: var(--paper-white);
    text-align: center; letter-spacing: .5px;
  }
  .back-bio {
    position: absolute; top: 545px; left: 150px; right: 36px;
    font-family: "EB Garamond", serif; font-size: 10.5px; line-height: 1.6;
    color: var(--body-text);
  }

  /* spine */
  .spine {
    position: relative; width: 60px; height: 100%;
    background: var(--spine);
    display: flex; flex-direction: column; align-items: center;
    padding: 40px 0 36px;
  }
  .spine-line {
    writing-mode: vertical-rl; white-space: nowrap;
  }
  .spine-title {
    font-family: "Cinzel Decorative", serif; font-weight: 700; font-size: 19px;
    color: var(--gold-mid); letter-spacing: 1px;
  }
  .spine-author {
    margin-top: auto;
    font-family: "Cinzel", serif; font-size: 24px; color: var(--paper-white);
  }

  /* front cover */
  .front-cover { position: relative; width: 505px; height: 100%; overflow: hidden; }
  .front-art {
    position: absolute; inset: 0;
    background:
      radial-gradient(ellipse 55% 30% at 45% 62%, rgba(255,236,150,.9), transparent 70%),
      radial-gradient(ellipse 40% 20% at 25% 45%, rgba(200,100,30,.55), transparent 70%),
      linear-gradient(180deg, var(--smoke) 0%, #4c3322 28%, #7b4a24 45%, var(--fire-orange) 58%, var(--fire-bright) 66%, #8a6430 80%, #3d2a18 100%);
  }
  .title-block { position: absolute; top: 70px; left: 0; right: 0; text-align: center; }
  .title-small, .title-large {
    font-family: "Cinzel Decorative", serif; font-weight: 900;
    background: linear-gradient(180deg, var(--gold-light) 0%, var(--gold-mid) 50%, var(--gold-deep) 100%);
    -webkit-background-clip: text; background-clip: text; color: transparent;
    filter: drop-shadow(0 2px 2px rgba(0,0,0,.7));
  }
  .title-small { display: block; font-size: 25px; letter-spacing: 1px; }
  .title-large { display: block; font-size: 86px; line-height: 1; margin-top: 2px; letter-spacing: 2px; }
  .back-title .title-small { font-size: 19px; }
  .back-title .title-large { font-size: 60px; }
  .front-author {
    position: absolute; bottom: 50px; left: 0; right: 0; text-align: center;
    font-family: "Cinzel", serif; font-size: 42px; color: var(--paper-white);
    text-shadow: 0 2px 4px rgba(0,0,0,.6);
  }
</style>
</head>
<body>
<div class="canvas">
  <div class="wrap">
    <section class="back-cover">
      <div class="back-art" role="img" aria-label="Cover artwork continued: a field of skulls glowing under a fiery sky, fading into darkness"></div>
      <div class="back-title">
        <span class="title-small">Thorns Beneath Winter</span>
        <span class="title-large">Ash</span>
      </div>
      <div class="back-body">
        <p>Lorem ipsum dolor sit amet, consectetur adipisicing elit, sed do eiusmod tempor incididunt ut labore et dolore magna aliqua. Ut enim ad minim veniam, quis nostrud exercitation ullamco laboris nisi ut aliquip ex ea commodo consequat. Duis aute irure dolor in reprehenderit in voluptate velit esse cillum dolore eu fugiat nulla pariatur. Excepteur sint occaecat cupidatat non proident, sunt in culpa qui officia deserunt mollit anim id est laborum.</p>
        <p>Sed ut perspiciatis unde omnis iste natus error sit voluptatem accusantium doloremque laudantium, totam rem aperiam, eaque ipsa quae ab illo inventore veritatis et quasi architecto beatae vitae dicta sunt explicabo. Nemo enim ipsam voluptatem quia voluptas sit aspernatur aut odit aut fugit, sed quia consequuntur magni dolores eos qui ratione voluptatem sequi nesciunt.</p>
        <p>Neque porro quisquam est, qui dolorem ipsum quia dolor sit amet, consectetur, adipisci velit, sed quia non numquam eius modi tempora incidunt ut labore et dolore magnam aliquam quaerat voluptatem.</p>
      </div>
      <div class="back-author">Merrick Tolvane</div>
      <p class="back-bio">Lorem ipsum dolor sit amet, consectetur adipiscing elit, sed do eiusmod tempor incididunt ut labore et dolore magna aliqua. Quis ipsum suspendisse ultrices gravida. Risus commodo viverra maecenas accumsan lacus vel facilisis.</p>
    </section>

    <section class="spine">
      <span class="spine-line spine-title">Thorns Beneath Winter Ash</span>
      <span class="spine-line spine-author">Merrick Tolvane</span>
    </section>

    <section class="front-cover">
      <div class="front-art" role="img" aria-label="Cover artwork: a hooded warrior with a sword stands on a mound of skulls, facing a burning ruined city under a fiery sky"></div>
      <h1 class="title-block">
        <span class="title-small">Thorns Beneath Winter</span>
        <span class="title-large">Ash</span>
      </h1>
      <p class="front-author">Merrick Tolvane</p>
    </section>
  </div>
</div>
</body>
</html>
```